LUMO animated presentation 2nd

Need:
Transform a power point presentation into an Animated Explainer Video. (I expect to need to submit further voice-over spoken text)
For:
The presentation is for LUMO, a 21st century-proof think tank and non-establishment advocate working for the protecting of human rights, democratic values.
Goal:
To increase name recognition, visibility and membership
Updates

Dear friends,

Having now spend more time on the brief I have to conclude that the presentation is simply too long to fit in an Explainer Video. The length is almost enough to hold a VEXO talk!

I don't want to leave you empty handed so I've created a very short call to action presentation of just 6 slides. I am looking forward to your proposals!

RK

Target Market(s)

Politically engaged public

Industry/Entity Type

N/a

Colors
EB3D1F
EC4F4E
F09395
F8D3D4
FCEDEE

Requirements
Must have
• The storyline per the attachment. Expected voice & character: A 60+ year old English male professor
Nice to have
• Let's discuss
Should not have
• Added content without consultation

```html
<!DOCTYPE html>
<html lang="en">
<head>
<meta charset="utf-8">
<title>LUMO – Animated Explainer Storyboard</title>
<link rel="stylesheet" href="https://fonts.googleapis.com/css2?family=Ubuntu:wght@300;400;500;700&family=Carlito:wght@400;700&display=swap">
<style>
  :root{
    --stage:#c00000;
    --red:#c8100f;
    --red-deep:#b00d0d;
    --pink-1:#f09395;
    --pink-2:#f8d3d4;
    --pink-3:#fcedee;
    --board:#e2dcda;
    --frame:#4a0f0f;
    --ink:#1c1c1c;
    --muted:#b9b9b9;
    --white:#ffffff;
    --head:"Ubuntu", sans-serif;
    --body:"Carlito", sans-serif;
  }
  *{margin:0;padding:0;box-sizing:border-box}
  html,body{width:1200px;height:800px;overflow:hidden;background:var(--stage)}
  .board{position:relative;width:1200px;height:800px;background:var(--stage);font-family:var(--body);color:var(--ink)}

  /* slide frames */
  .slide{position:absolute;width:333px;height:188px;background:var(--white);overflow:hidden;box-shadow:0 3px 10px rgba(70,0,0,.35)}
  .col-1{left:71px}.col-2{left:433px}.col-3{left:795px}
  .row-1{top:83px}.row-2{top:295px}.row-3{top:505px}
  .abs{position:absolute}

  /* recurring slide footer */
  .footer-rule-v{position:absolute;left:10px;top:155px;width:.6px;height:33px;background:var(--red)}
  .footer-rule-h{position:absolute;left:0;top:180px;width:86px;height:.6px;background:var(--red)}
  .footer-name{position:absolute;left:17px;top:163px;font-family:var(--body);font-size:6px;line-height:7.6px;color:var(--ink)}
  .footer-brand{position:absolute;right:16px;bottom:12px;font-family:var(--head);font-weight:700;font-size:7px;color:var(--red)}
  .footer-credit{position:absolute;right:14px;bottom:6px;font-family:var(--body);font-size:3px;color:var(--ink)}
  .footer-credit b{font-weight:700}

  /* decorative dot map placeholder */
  .dot-map{position:absolute;border-radius:46% 40% 44% 52%/50% 42% 56% 48%;
    background:radial-gradient(ellipse at 55% 50%,var(--red) 0%,#d8484a 35%,var(--pink-1) 62%,rgba(248,211,212,0) 78%)}
  .dot-map--faint{background:radial-gradient(ellipse at 55% 50%,var(--pink-2) 0%,var(--pink-3) 55%,rgba(252,237,238,0) 78%)}

  .slide-title{position:absolute;left:14px;top:17px;font-family:var(--head);font-weight:700;font-size:12.5px;letter-spacing:.3px;color:var(--red)}

  /* cover */
  .cover-brand{position:absolute;left:45px;top:64px;font-family:var(--head);font-weight:700;font-size:31px;color:var(--red);letter-spacing:.5px}
  .cover-tagline{position:absolute;left:46px;top:96px;font-family:var(--body);font-size:7px;line-height:8.5px;color:var(--ink)}
  .cover-note{position:absolute;right:36px;bottom:16px;width:80px;text-align:center;font-size:3px;line-height:3.6px;color:var(--ink)}
  .cover-note-brand{position:absolute;right:12px;bottom:16px;font-family:var(--head);font-weight:700;font-size:7px;color:var(--red);border-left:.6px solid var(--red);padding-left:3px}
  .slide--intro .fade{opacity:.28}
  .slide--intro .cover-tagline{color:var(--muted)}

  /* menu list */
  .menu-item{position:absolute;left:111px;width:107px}
  .menu-head{display:block;font-family:var(--head);font-weight:700;font-size:11px;line-height:12px;color:var(--red);border-bottom:.6px solid var(--red);border-left:.6px solid var(--red);padding-left:1px}
  .menu-tag{display:inline-block;margin-top:1px;background:var(--red);color:var(--white);font-family:var(--head);font-weight:500;font-size:5.6px;line-height:8px;padding:0 7px 0 3px;clip-path:polygon(0 0,100% 0,calc(100% - 4px) 100%,0 100%)}

  /* vision */
  .vision-row{position:absolute;left:32px;width:194px;height:31px}
  .vision-arrow{position:absolute;inset:0;background:var(--board);clip-path:polygon(0 0,calc(100% - 12px) 0,100% 50%,calc(100% - 12px) 100%,0 100%)}
  .vision-key{position:absolute;left:0;top:0;width:89px;height:31px;background:var(--red);border-radius:5px 0 0 5px;clip-path:polygon(0 0,92% 0,100% 50%,92% 100%,0 100%);color:var(--white);font-family:var(--head);font-weight:500;font-size:8px;display:flex;align-items:center;justify-content:center}
  .vision-value{position:absolute;left:98px;top:0;height:31px;display:flex;align-items:center;font-family:var(--head);font-weight:500;font-size:6.4px;line-height:8px;color:var(--red)}
  .vision-note{position:absolute;left:233px;width:64px;font-size:4.3px;line-height:5.3px;color:var(--ink)}

  /* illustration placeholders */
  .illustration{position:absolute}
  .teacher{background:linear-gradient(180deg,#f1ece9 0%,#b9b3b0 45%,#8a8482 100%)}
  .chalkboard{position:absolute;background:var(--board);border:5px solid var(--frame);border-right:none}

  /* mechanism */
  .mech-icon{position:absolute;width:36px;height:36px;border:1px solid var(--red);border-radius:50%;display:flex;align-items:center;justify-content:center}
  .mech-icon span{display:block;width:20px;height:20px;border-radius:50%;background:linear-gradient(160deg,#8a5a4a,#5a2c24)}
  .mech-label{position:absolute;width:70px;text-align:center;font-family:var(--head);font-weight:700;font-size:5.3px;line-height:6.6px;color:var(--red)}

  /* where */
  .where-col{position:absolute;width:130px;text-align:center}
  .where-lead{font-weight:700;font-size:7px;line-height:8.5px;color:var(--ink)}
  .where-btn{display:block;margin:7px auto 0;width:110px;height:18px;line-height:18px;background:var(--red);color:var(--white);border-radius:2px;font-size:7px;font-weight:700}
  .where-foot{position:absolute;left:83px;top:110px;width:160px;text-align:center;font-weight:700;font-size:7px;line-height:8.5px}
  .where-foot em{font-style:normal;color:var(--red)}

  /* next step */
  .next-copy{position:absolute;left:20px;top:45px;width:210px;font-size:7.4px;line-height:10.6px}
  .contact-tag{position:absolute;left:0;top:86px;width:53px;height:10px;background:var(--red);color:var(--white);font-family:var(--head);font-weight:500;font-size:6px;line-height:10px;padding-left:16px;clip-path:polygon(0 0,calc(100% - 4px) 0,100% 50%,calc(100% - 4px) 100%,0 100%)}
  .contact-name{position:absolute;left:20px;top:101px;font-family:var(--head);font-weight:500;font-size:8.6px}
  .contact-line{position:absolute;left:20px;display:flex;align-items:center;gap:3px;font-size:5.8px}
  .contact-line svg{width:8px;height:8px}

  /* board caption */
  .caption-rule-v{position:absolute;left:41px;top:700px;width:1.4px;height:100px;background:var(--white)}
  .caption-rule-h{position:absolute;left:0;top:774px;width:269px;height:1.4px;background:var(--white)}
  .caption-title{position:absolute;left:49px;top:722px;font-family:var(--head);font-weight:500;font-size:20px;line-height:24px;color:var(--white)}
  .caption-title .light{font-weight:300}
  .specs{position:absolute;right:72px;top:722px;text-align:right;font-family:var(--head);font-size:19.5px;line-height:30px;color:var(--white)}
  .specs .label{font-weight:300;margin-right:8px}
  .specs .value{font-weight:500}
</style>
</head>
<body>
<main class="board">

  <!-- 1 intro fade -->
  <section class="slide col-1 row-1 slide--intro">
    <div class="fade">
      <div class="cover-brand">LUMO</div>
      <div class="dot-map abs" style="left:198px;top:22px;width:140px;height:140px" role="img" aria-label="Red dot-matrix world map pattern"></div>
      <div class="cover-note">This document may not be reproduced or shared without the explicit consent of the author.</div>
      <div class="cover-note-brand">LUMO</div>
      <div class="footer-credit"><b>Rein Kalden</b> - All Rights Reserved - 2021</div>
      <div class="footer-name">Lumen Union of<br>Modern Observers</div>
      <div class="footer-rule-v"></div><div class="footer-rule-h"></div>
    </div>
    <p class="cover-tagline" style="left:36px">For sovereignty, democracy and<br>the pursuit of meaning</p>
  </section>

  <!-- 2 cover -->
  <section class="slide col-2 row-1">
    <div class="cover-brand">LUMO</div>
    <p class="cover-tagline">For sovereignty, democracy and<br>the pursuit of meaning</p>
    <div class="dot-map abs" style="left:186px;top:22px;width:150px;height:140px" role="img" aria-label="Red dot-matrix world map pattern"></div>
    <div class="cover-note">This document may not be reproduced or shared without the explicit consent of the author.</div>
    <div class="cover-note-brand">LUMO</div>
    <div class="footer-credit"><b>Rein Kalden</b> - All Rights Reserved - 2021</div>
    <div class="footer-name">Lumen Union of<br>Modern Observers</div>
    <div class="footer-rule-v"></div><div class="footer-rule-h"></div>
  </section>

  <!-- 3 menu with transition bands -->
  <section class="slide col-3 row-1">
    <div class="dot-map dot-map--faint" style="left:170px;top:20px;width:165px;height:140px" role="img" aria-label="Faint dot-matrix world map pattern"></div>
    <div class="menu-item" style="top:47px"><span class="menu-head">LUMO</span><span class="menu-tag">MEMBERSHIP</span></div>
    <div class="menu-item" style="top:83px;width:115px"><span class="menu-head">LUMO</span><span class="menu-tag">INTERNATIONAL CONFERENCE</span></div>
    <div class="menu-item" style="top:120px"><span class="menu-head">LUMO</span><span class="menu-tag">MAGAZINE</span></div>
    <svg class="abs" style="left:0;top:0" width="333" height="188" viewBox="0 0 333 188" aria-hidden="true">
      <polygon points="34,0 58,0 0,56 0,32" fill="#d8484a"/>
      <polygon points="0,126 84,46 142,46 0,162" fill="var(--red)"/>
      <polygon points="333,12 333,66 262,142 208,142" fill="var(--red)"/>
      <polygon points="333,118 333,142 306,142" fill="var(--red)"/>
    </svg>
    <div class="footer-credit"><b>Rein Kalden</b> - All Rights Reserved - 2021</div>
    <div class="footer-name">Lumen Union of<br>Modern Observers</div>
    <div class="footer-rule-v"></div><div class="footer-rule-h"></div>
  </section>

  <!-- 4 vision -->
  <section class="slide col-1 row-2">
    <h2 class="slide-title">LUMO'S VISION</h2>
    <div class="vision-row" style="top:44px"><div class="vision-arrow"></div><div class="vision-key">Unifying ideal</div><div class="vision-value">Humans,<br>not transhumans</div></div>
    <div class="vision-row" style="top:80px"><div class="vision-arrow"></div><div class="vision-key">Uncontroversial</div><div class="vision-value">Evolution,<br>not revolution</div></div>
    <div class="vision-row" style="top:115px"><div class="vision-arrow"></div><div class="vision-key">Scalable globally</div><div class="vision-value">Target market,<br>200-300 million<br>peoples</div></div>
    <p class="vision-note" style="top:49px">We work for a society in which people are recognized first as human beings and second as citizens</p>
    <p class="vision-note" style="top:80px">Building on Elias Marlow' ideal of a "government of laws, not of men," we should in fact strive to become "peoples of laws, not of governments."</p>
    <div class="footer-brand">LUMO</div>
    <div class="footer-credit"><b>Rein Kalden</b> - All Rights Reserved - 2021</div>
    <div class="footer-name">Lumen Union of<br>Modern Observers</div>
    <div class="footer-rule-v"></div><div class="footer-rule-h"></div>
  </section>

  <!-- 5 transition to mechanism -->
  <section class="slide col-2 row-2">
    <div class="chalkboard" style="left:120px;top:20px;width:213px;height:155px"></div>
    <div class="illustration teacher" style="left:0;top:98px;width:86px;height:90px" role="img" aria-label="Illustrated professor pointing at the board"></div>
    <svg class="abs" style="left:0;top:0" width="333" height="188" viewBox="0 0 333 188" aria-hidden="true">
      <polygon points="0,0 250,0 206,46 128,46 0,172" fill="var(--red)"/>
      <polygon points="333,8 333,62 250,140 172,140" fill="var(--red)"/>
      <polygon points="333,96 333,188 92,188" fill="var(--red)"/>
      <polygon points="40,64 52,64 0,114 0,102" fill="var(--white)"/>
    </svg>
    <div class="footer-credit"><b>Rein Kalden</b> - All Rights Reserved - 2021</div>
    <div class="footer-name">Lumen Union of<br>Modern Observers</div>
    <div class="footer-rule-v"></div><div class="footer-rule-h"></div>
  </section>

  <!-- 6 mechanism -->
  <section class="slide col-3 row-2">
    <h2 class="slide-title" style="left:16px">MECHANISM</h2>
    <div class="chalkboard" style="left:115px;top:20px;width:218px;height:155px;border-radius:4px 0 0 4px"></div>
    <div class="mech-icon" style="left:166px;top:37px" role="img" aria-label="Scales of justice icon"><span></span></div>
    <div class="mech-icon" style="left:237px;top:37px" role="img" aria-label="Law book icon"><span></span></div>
    <div class="mech-icon" style="left:166px;top:105px" role="img" aria-label="Briefcase and document icon"><span></span></div>
    <div class="mech-icon" style="left:237px;top:105px" role="img" aria-label="Speaker at lectern icon"><span></span></div>
    <p class="mech-label" style="left:149px;top:82px">EMPOWERING THE<br>NON-ESTABLISHMENT</p>
    <p class="mech-label" style="left:220px;top:82px">CRITICAL MASS</p>
    <p class="mech-label" style="left:147px;top:149px;width:74px">LEGAL REPRESENTATION</p>
    <p class="mech-label" style="left:218px;top:149px;width:74px">POLITICAL RELEVANCY</p>
    <div class="illustration teacher" style="left:2px;top:52px;width:130px;height:136px" role="img" aria-label="Illustrated senior professor holding a red LUMO book and pointing at the board"></div>
    <div class="footer-brand">LUMO</div>
    <div class="footer-credit"><b>Rein Kalden</b> - All Rights Reserved - 2021</div>
    <div class="footer-name">Lumen Union of<br>Modern Observers</div>
    <div class="footer-rule-v"></div><div class="footer-rule-h"></div>
  </section>

  <!-- 7 how -->
  <section class="slide col-1 row-3">
    <h2 class="slide-title" style="left:16px">HOW</h2>
    <div class="dot-map dot-map--faint" style="left:190px;top:22px;width:150px;height:145px" role="img" aria-label="Faint dot-matrix world map pattern"></div>
    <div class="menu-item" style="top:49px"><span class="menu-head">LUMO</span><span class="menu-tag">MEMBERSHIP</span></div>
    <div class="menu-item" style="top:85px;width:106px"><span class="menu-head">LUMO</span><span class="menu-tag">INTERNATIONAL CONFERENCE</span></div>
    <div class="menu-item" style="top:121px"><span class="menu-head">LUMO</span><span class="menu-tag">MAGAZINE</span></div>
    <div class="footer-brand">LUMO</div>
    <div class="footer-credit"><b>Rein Kalden</b> - All Rights Reserved - 2021</div>
    <div class="footer-name">Lumen Union of<br>Modern Observers</div>
    <div class="footer-rule-v"></div><div class="footer-rule-h"></div>
  </section>

  <!-- 8 where -->
  <section class="slide col-2 row-3">
    <h2 class="slide-title" style="left:15px">WHERE</h2>
    <div class="dot-map dot-map--faint" style="left:180px;top:22px;width:160px;height:145px" role="img" aria-label="Faint dot-matrix world map pattern"></div>
    <div class="where-col" style="left:26px;top:49px">
      <p class="where-lead">You can sign up easily and anonymously here:</p>
      <span class="where-btn">www.lumo-org.com/join-us</span>
    </div>
    <div class="where-col" style="left:178px;top:49px">
      <p class="where-lead">You can also read and sign our symbolic Declaration of Sovereignty here:</p>
      <span class="where-btn">charterofselfrule.org</span>
    </div>
    <p class="where-foot">If you <em>sign in</em> you'll get a very nice charter in pdf in your <em>inbox</em>!</p>
    <div class="footer-brand">LUMO</div>
    <div class="footer-credit"><b>Rein Kalden</b> - All Rights Reserved - 2021</div>
    <div class="footer-name">Lumen Union of<br>Modern Observers</div>
    <div class="footer-rule-v"></div><div class="footer-rule-h"></div>
  </section>

  <!-- 9 next step -->
  <section class="slide col-3 row-3">
    <h2 class="slide-title" style="left:17px">NEXT STEP</h2>
    <p class="next-copy">We are looking for members, partners and capital to support this initiative, and start organizing the first (online) symposium and introduction of the LUMO magazine for Q2 of next year.</p>
    <div class="contact-tag">Contact</div>
    <p class="contact-name">Rein Kalden</p>
    <p class="contact-line" style="top:115px">
      <svg viewBox="0 0 10 10"><circle cx="5" cy="5" r="5" fill="var(--red)"/><path d="M3.3 2.6l1 1-.5.7c.4.8 1 1.4 1.8 1.8l.7-.5 1 1-.7.8C4.8 7.2 2.8 5.2 2.6 3.3z" fill="#fff"/></svg>0031655501234</p>
    <p class="contact-line" style="top:127px">
      <svg viewBox="0 0 10 10"><circle cx="5" cy="5" r="5" fill="var(--red)"/><rect x="2.6" y="3.3" width="4.8" height="3.4" fill="none" stroke="#fff" stroke-width=".6"/><path d="M2.6 3.3L5 5.2l2.4-1.9" fill="none" stroke="#fff" stroke-width=".6"/></svg>rein@lumo-org.com</p>
    <p class="contact-line" style="top:139px">
      <svg viewBox="0 0 10 10"><circle cx="5" cy="5" r="5" fill="var(--red)"/><circle cx="5" cy="5" r="2.6" fill="none" stroke="#fff" stroke-width=".6"/><path d="M2.4 5h5.2M5 2.4c-1.3 1.5-1.3 3.7 0 5.2M5 2.4c1.3 1.5 1.3 3.7 0 5.2" fill="none" stroke="#fff" stroke-width=".5"/></svg>www.lumo-org.com</p>
    <div class="footer-brand">LUMO</div>
    <div class="footer-credit"><b>Rein Kalden</b> - All Rights Reserved - 2021</div>
    <div class="footer-name">Lumen Union of<br>Modern Observers</div>
    <div class="footer-rule-v"></div><div class="footer-rule-h"></div>
  </section>

  <!-- caption -->
  <div class="caption-rule-v"></div>
  <div class="caption-rule-h"></div>
  <h1 class="caption-title">Lumen Union <span class="light">of</span><br>Modern Observers</h1>
  <div class="specs">
    <p><span class="label">Resolution</span><span class="value">1920 x 1080 px | 25 FPS</span></p>
    <p><span class="label">Duration</span><span class="value">0:02:00:00</span></p>
  </div>

</main>
</body>
</html>
```